Consulting Executive Needs Personal InfoGraphic One Pager

I need a one-page personal promo piece which contains a number of infographics highlighting core aspects of my professional experience and qualifications. This is meant to visually illustrate the talents and background I can bring to prospective employers. The final design must fit onto on standard U.S. Letter size page, include the categories of information I want represented in "mini infographics", and be a bit fun and quirky. No restriction on color scheme, though I do love purple and would be happy to see that as a primary color. I'm providing a spec which lists out which information needs to be included.

Industry/Entity Type

Consulting

Requirements
Must have
• Must fit onto a single U.S. letter size page (8.5" x 11")

```html
<!DOCTYPE html>
<html lang="en">
<head>
<meta charset="utf-8">
<title>Why You Should Hire Me</title>
<link rel="stylesheet" href="https://fonts.googleapis.com/css2?family=Libre+Baskerville:wght@400;700&family=Source+Sans+3:wght@400;600;700&display=swap">
<style>
  :root {
    --navy: #15154a;
    --violet: #6b6cf2;
    --violet-light: #7d7ef6;
    --ink: #15154a;
    --white: #ffffff;
    --paper: #ffffff;
  }
  html, body { margin: 0; padding: 0; overflow: hidden; }
  body { width: 985px; height: 1200px; background: var(--paper); position: relative;
         font-family: "Source Sans 3", Arial, sans-serif; color: var(--ink); }
  .page { position: absolute; inset: 0; overflow: hidden; }

  .header-band { position: absolute; left: 0; top: 53px; width: 985px; height: 40px; background: var(--navy); }
  .header-stripe { position: absolute; left: 0; top: 93px; width: 985px; height: 8px; background: var(--violet-light); }
  .header-title { position: absolute; right: 138px; top: 56px; margin: 0;
                  font-family: "Libre Baskerville", Georgia, serif; font-weight: 700;
                  font-size: 27px; color: var(--white); letter-spacing: -0.3px; }
  .header-tagline { position: absolute; right: 142px; top: 90px; margin: 0;
                    font-family: "Libre Baskerville", Georgia, serif; font-size: 9px; color: var(--navy); }
  .question-mark { position: absolute; left: 853px; top: 12px; width: 62px; height: 96px; }

  .infographic { position: absolute; left: 0; top: 0; width: 985px; height: 644px; }
  .infographic text { font-family: "Source Sans 3", Arial, sans-serif; }
  .label-text { fill: var(--white); font-weight: 600; }
  .list-text { fill: var(--navy); font-weight: 600; }

  .factoids { position: absolute; left: 48px; top: 1048px; display: flex; align-items: center; gap: 14px; }
  .factoids-icon { width: 50px; height: 50px; }
  .factoids-title { margin: 0; font-family: "Libre Baskerville", Georgia, serif; font-weight: 700;
                    font-size: 27px; color: var(--navy); }

  .footer-stripe { position: absolute; left: 0; top: 1125px; width: 985px; height: 11px; background: var(--violet-light); }
  .footer-band { position: absolute; left: 0; top: 1136px; width: 985px; height: 64px; background: var(--navy); }
  .contact { position: absolute; right: 22px; top: 1145px; margin: 0; text-align: right;
             font-size: 17px; line-height: 21px; color: var(--white); font-style: normal; }
  .contact strong { font-weight: 700; }
</style>
</head>
<body>
<main class="page">
  <div class="header-band"></div>
  <div class="header-stripe"></div>
  <h1 class="header-title">Why You Should Hire Me</h1>
  <p class="header-tagline">Well, I think you know it</p>
  <svg class="question-mark" viewBox="0 0 62 96" aria-hidden="true">
    <text x="31" y="78" text-anchor="middle" font-family="Libre Baskerville, Georgia, serif" font-weight="700"
          font-size="100" fill="#15154a" stroke="#ffffff" stroke-width="3" paint-order="stroke">?</text>
  </svg>

  <svg class="infographic" viewBox="0 0 612 400" aria-label="Career infographics">
    <!-- installs bubble -->
    <path d="M46,101 H150 Q160,101 160,111 V166 L170,186 L149,175 H50 Q40,175 40,165 V111 Q40,101 46,101 Z" fill="#15154a"/>
    <rect x="52" y="108" width="99" height="60" rx="7" fill="#6b6cf2"/>
    <rect x="35" y="86" width="90" height="17" fill="#15154a"/>
    <text class="label-text" x="41" y="99" font-size="10.5">25+ Apex installs</text>
    <g class="list-text" font-size="6.6">
      <text x="57" y="119">1.Lakeshore Clinic</text>
      <text x="57" y="128">2.UVHS</text>
      <text x="57" y="137">3.Kessinger Health</text>
      <text x="57" y="146">4.Gulfcoast Hospitals</text>
      <text x="57" y="155">5.University of Coral Bay</text>
    </g>

    <!-- roles bubble -->
    <path d="M222,122 H298 Q305,122 305,129 V186 Q305,193 298,193 H232 L204,201 L218,186 Q214,182 214,176 V130 Q214,122 222,122 Z" fill="#15154a"/>
    <rect x="222" y="128" width="77" height="58" rx="6" fill="#6b6cf2"/>
    <rect x="235" y="110" width="65" height="17" fill="#15154a"/>
    <text class="label-text" x="242" y="122.5" font-size="10">Worked as</text>
    <g class="list-text" font-size="5.2">
      <text x="228" y="139">1.Project Director</text>
      <text x="228" y="146.5">2.Program Manager</text>
      <text x="228" y="154">3.Executive Advisor</text>
      <text x="228" y="161.5">4.Clinical Process Redesign</text>
      <text x="228" y="169">5.Project Rescue</text>
    </g>

    <!-- gears -->
    <circle cx="172" cy="188" r="13" fill="#ffffff" stroke="#15154a" stroke-width="3"/>
    <circle cx="172" cy="188" r="6" fill="#ffffff" stroke="#15154a" stroke-width="3"/>
    <circle cx="187" cy="157" r="8" fill="#ffffff" stroke="#15154a" stroke-width="2.5"/>
    <circle cx="187" cy="157" r="3.5" fill="#15154a"/>
    <circle cx="203" cy="172" r="5" fill="#ffffff" stroke="#15154a" stroke-width="2"/>
    <circle cx="203" cy="172" r="1.8" fill="#15154a"/>

    <!-- implementation label with clock -->
    <line x1="172" y1="201" x2="172" y2="207" stroke="#15154a" stroke-width="2"/>
    <line x1="128" y1="221" x2="250" y2="221" stroke="#15154a" stroke-width="1.5"/>
    <circle cx="118" cy="212" r="8.5" fill="#15154a"/>
    <circle cx="118" cy="213" r="5.5" fill="#ffffff"/>
    <path d="M118,210 V213.5 H120.5" stroke="#15154a" stroke-width="1.2" fill="none"/>
    <circle cx="112" cy="204" r="2.4" fill="#15154a"/>
    <circle cx="124" cy="204" r="2.4" fill="#15154a"/>
    <text class="list-text" x="132" y="217" font-size="7" font-weight="700">Apex Implementation Experience</text>

    <!-- plus connector -->
    <line x1="250" y1="221" x2="266" y2="212" stroke="#15154a" stroke-width="1.5"/>
    <circle cx="276" cy="205" r="14" fill="#15154a"/>
    <circle cx="276" cy="205" r="10.5" fill="#ffffff"/>
    <circle cx="276" cy="205" r="8.5" fill="#15154a"/>
    <path d="M276,199 V211 M270,205 H282" stroke="#ffffff" stroke-width="3"/>

    <!-- expertise box -->
    <path d="M304,205 L452,207 L455,386 L308,384 Z" fill="#15154a"/>
    <path d="M316,213 L446,214 L448,378 L318,376 Z" fill="#6b6cf2"/>
    <rect x="295" y="187" width="161" height="21" fill="#15154a"/>
    <text class="label-text" x="302" y="202" font-size="12.5">Apex Application Expertise</text>
    <g class="list-text" font-size="7.8">
      <text x="321" y="222">i.ApexCare Ambulatory</text>
      <text x="321" y="232.4" textLength="121" lengthAdjust="spacingAndGlyphs">ii.ApexCare Inpatient Clin Doc and Orders</text>
      <text x="321" y="242.8">iii.MyPortal</text>
      <text x="321" y="253.2">iv.Tempo</text>
      <text x="321" y="263.6">v.Overture/ADT</text>
      <text x="321" y="274">vi.RAPID</text>
      <text x="321" y="284.4">vii.OpClock</text>
      <text x="321" y="294.8">viii.Birch</text>
      <text x="321" y="305.2">ix.Lantern</text>
      <text x="321" y="315.6">x.Steadfast HB &amp; PB</text>
      <text x="321" y="326">xi.Heron</text>
      <text x="321" y="336.4">xii.Nurse Triage</text>
      <text x="321" y="346.8">xiii.Care Anywhere</text>
      <text x="321" y="357.2">xiv.Health Link</text>
      <text x="321" y="367.6">xv.Lumen</text>
    </g>

    <!-- consulting stats -->
    <line x1="460" y1="168" x2="447" y2="188" stroke="#15154a" stroke-width="2"/>
    <path d="M398,94 L590,92 L588,172 L402,170 Z" fill="#15154a"/>
    <path d="M406,99 L584,97 L582,164 L410,162 Z" fill="#6b6cf2"/>
    <rect x="388" y="74" width="190" height="21" fill="#15154a"/>
    <text class="label-text" x="393" y="89" font-size="12">Consulting Firm Start Up Stats</text>
    <g class="list-text" font-size="7.2">
      <text x="412" y="107">i.Number of firms built from the ground floor: 4</text>
      <text x="412" y="116">ii.Number of business plans authored: 8</text>
      <text x="412" y="125">iii.Number of marketing plans authored: 6</text>
      <text x="412" y="134">iv.Number of core consulting methodologies</text>
      <text x="412" y="143">developed: 4</text>
    </g>

    <!-- calculator icon -->
    <rect x="350" y="92" width="28" height="33" rx="3" fill="#15154a"/>
    <rect x="354" y="96" width="20" height="6" fill="#ffffff"/>
    <g fill="#ffffff">
      <rect x="354" y="105" width="4" height="4"/><rect x="362" y="105" width="4" height="4"/><rect x="370" y="105" width="4" height="4"/>
      <rect x="354" y="112" width="4" height="4"/><rect x="362" y="112" width="4" height="4"/><rect x="370" y="112" width="4" height="4"/>
      <rect x="354" y="119" width="4" height="3"/><rect x="362" y="119" width="4" height="3"/><rect x="370" y="119" width="4" height="3"/>
    </g>
  </svg>

  <section class="factoids">
    <svg class="factoids-icon" viewBox="0 0 50 50" aria-hidden="true">
      <rect x="3" y="9" width="36" height="36" rx="4" fill="none" stroke="#6b6cf2" stroke-width="5"/>
      <path d="M17,33 L19,26 L40,5 L46,11 L25,32 Z" fill="#6b6cf2" stroke="#ffffff" stroke-width="2"/>
    </svg>
    <h2 class="factoids-title">Check Out my Personal “factoids”</h2>
  </section>

  <div class="footer-stripe"></div>
  <div class="footer-band"></div>
  <address class="contact">
    <strong>J. Morgan Ellsworth,</strong> 1427 <strong>Alder Lane,</strong> Fairview, CA 94000,<br>
    morgan_ellsworth@example.com, <strong>mobile:</strong> 555.014.2297
  </address>
</main>
</body>
</html>
```